Lounge Night Poster

We need an attractive poster for our new lounge/night club in San Francisco called Velvora Nightclub, promoting our new event, "Lantern Drift". We will have a live band and Asian singers performing during the night. It is like a lounge where people can chill and have a sip. It will open on July 21.

Industry/Entity Type

Club

```html
<!DOCTYPE html>
<html lang="en">
<head>
<meta charset="utf-8">
<title>Lantern Drift — Velvora Nightclub</title>
<link href="https://fonts.googleapis.com/css2?family=Uncial+Antiqua&family=Oswald:wght@400;600&display=swap" rel="stylesheet">
<style>
  :root {
    --ink-indigo: #1c0c5e;
    --ink-violet: #5a2bd0;
    --ink-bright: #7040e6;
    --glow-amber: #ffd23a;
    --glow-orange: #ff7a2a;
    --neon-magenta: #c4208a;
    --deep-plum: #3a0f4a;
    --haze-lilac: #c9b8f2;
    --haze-white: #f1ecff;
  }
  * { margin: 0; padding: 0; box-sizing: border-box; }
  html, body {
    width: 848px;
    height: 1200px;
    overflow: hidden;
    background: var(--deep-plum);
  }
  .poster {
    position: relative;
    width: 848px;
    height: 1200px;
    overflow: hidden;
  }
  .poster__photo {
    position: absolute;
    inset: 0;
    background:
      radial-gradient(ellipse 210px 190px at 450px 330px, rgba(255,236,110,0.95), rgba(255,210,58,0) 100%),
      radial-gradient(ellipse 430px 330px at 440px 430px, rgba(255,122,42,0.85), rgba(255,122,42,0) 100%),
      radial-gradient(ellipse 260px 220px at 790px 420px, rgba(255,210,70,0.75), rgba(255,200,60,0) 100%),
      radial-gradient(ellipse 220px 180px at 40px 430px, rgba(255,200,80,0.7), rgba(255,190,70,0) 100%),
      radial-gradient(ellipse 300px 200px at 600px 130px, rgba(255,230,120,0.45), rgba(255,230,120,0) 100%),
      radial-gradient(ellipse 500px 260px at 430px 1010px, rgba(241,236,255,0.95), rgba(201,184,242,0) 100%),
      radial-gradient(ellipse 140px 500px at 0px 900px, rgba(90,40,170,0.55), rgba(90,40,170,0) 100%),
      linear-gradient(180deg, #3e0d34 0%, #6e1a5e 16%, #b43a8c 40%, #a05ac8 60%, #b9a2ee 80%, #8e78d8 100%);
  }
  .poster__title {
    position: absolute;
    left: 0;
    right: 0;
    top: 712px;
    text-align: center;
    font-family: "Uncial Antiqua", fantasy;
    font-weight: 400;
    font-size: 108px;
    line-height: 140px;
    letter-spacing: 1px;
    background: linear-gradient(160deg, var(--ink-indigo) 0%, var(--ink-violet) 35%, var(--ink-indigo) 55%, var(--ink-bright) 75%, var(--ink-indigo) 100%);
    -webkit-background-clip: text;
    background-clip: text;
    color: transparent;
  }
  .poster__date {
    position: absolute;
    left: 0;
    right: 0;
    top: 1036px;
    text-align: center;
    font-family: "Oswald", sans-serif;
    font-weight: 400;
    font-size: 42px;
    line-height: 56px;
    letter-spacing: 2px;
    color: var(--ink-indigo);
  }
  .poster__date strong { font-weight: 600; }
</style>
</head>
<body>
  <main class="poster">
    <div class="poster__photo" role="img" aria-label="Photo of a woman in mirrored sunglasses running her hands through her hair, lit in warm orange and magenta neon above a glowing lounge bar counter"></div>
    <h1 class="poster__title">LANTERN<br>DRIFT</h1>
    <p class="poster__date">OPENS ON <strong>JULY 21</strong></p>
  </main>
</body>
</html>
```